Accounting firm needing business card / letterhead designed
Marcus T. Elbering, CPA
marcus@fernquill.com
www.fernquill.com
482 N Harlow Ave Ashcombe, WI 43719
608-555-0172

```html
<!DOCTYPE html>
<html lang="en">
<head>
<meta charset="utf-8">
<title>Fernquill business card</title>
<link href="https://fonts.googleapis.com/css2?family=Lato:wght@400;700;900&display=swap" rel="stylesheet">
<style>
  :root {
    --navy: #262262;
    --green: #8dc63f;
    --paper: #ffffff;
    --ink: #1a1a1a;
    --backdrop: #ececec;
  }
  * { margin: 0; padding: 0; box-sizing: border-box; }
  html, body {
    width: 1200px; height: 586px; overflow: hidden;
    background: var(--backdrop);
    font-family: 'Lato', Arial, sans-serif;
  }
  .stage { position: relative; width: 1200px; height: 586px; }
  .card {
    position: absolute; top: 129px;
    width: 502px; height: 300px;
    overflow: hidden;
  }
  .card--front { left: 61px; background: var(--navy); }
  .card--back { left: 619px; background: var(--paper); }

  .wordmark {
    position: absolute; left: 0; right: 0;
    text-align: center;
    font-weight: 900;
    letter-spacing: 0.04em;
    line-height: 1;
  }
  .card--front .wordmark { top: 100px; font-size: 48px; color: var(--paper); }
  .card--back .wordmark { top: 46px; font-size: 34px; color: var(--navy); }

  .website {
    position: absolute; left: 0; right: 0; top: 256px;
    text-align: center;
    color: var(--paper);
    font-size: 11px; font-weight: 700;
    letter-spacing: 0.22em;
  }

  .contact-list { position: absolute; left: 27px; top: 198px; list-style: none; }
  .contact-list li {
    display: flex; align-items: center;
    height: 25px;
    font-size: 11.5px; color: var(--ink);
  }
  .contact-icon { width: 18px; height: 18px; margin-right: 6px; flex: none; }

  .holder { position: absolute; right: 30px; top: 218px; text-align: right; }
  .holder-name { font-size: 17px; font-weight: 700; color: var(--navy); line-height: 1.1; }
  .holder-title { font-size: 11px; color: var(--ink); margin-top: 2px; }

  .edge-band { position: absolute; left: 0; bottom: 0; width: 502px; height: 16px; }
</style>
</head>
<body>
<main class="stage">
  <section class="card card--front" aria-label="Card front">
    <div class="wordmark">FERNQUILL</div>
    <div class="website">www.fernquill.com</div>
  </section>

  <section class="card card--back" aria-label="Card back">
    <div class="wordmark">FERNQUILL</div>

    <ul class="contact-list">
      <li>
        <svg class="contact-icon" viewBox="0 0 18 18" aria-hidden="true">
          <circle cx="9" cy="9" r="9" fill="var(--navy)"/>
          <path d="M5 7.5c0-1.2 1.8-2.2 4-2.2s4 1 4 2.2v.8h-2.2v-.9H7.2v.9H5z" fill="#fff"/>
          <rect x="6" y="8.6" width="6" height="3.8" rx="0.8" fill="#fff"/>
        </svg>
        608-555-0172
      </li>
      <li>
        <svg class="contact-icon" viewBox="0 0 18 18" aria-hidden="true">
          <circle cx="9" cy="9" r="9" fill="var(--navy)"/>
          <rect x="4.5" y="5.8" width="9" height="6.4" fill="none" stroke="#fff" stroke-width="1"/>
          <path d="M4.5 5.8 9 9.6l4.5-3.8" fill="none" stroke="#fff" stroke-width="1"/>
        </svg>
        marcus@fernquill.com
      </li>
      <li>
        <svg class="contact-icon" viewBox="0 0 18 18" aria-hidden="true">
          <circle cx="9" cy="9" r="9" fill="var(--navy)"/>
          <rect x="6" y="4" width="6" height="10" fill="#fff"/>
          <path d="M7.3 5.5h1.2M9.5 5.5h1.2M7.3 7.5h1.2M9.5 7.5h1.2M7.3 9.5h1.2M9.5 9.5h1.2" stroke="var(--navy)" stroke-width="0.9"/>
        </svg>
        482 N Harlow Ave Ashcombe, WI 43719
      </li>
    </ul>

    <div class="holder">
      <div class="holder-name">Marcus T. Elbering</div>
      <div class="holder-title">CPA</div>
    </div>

    <svg class="edge-band" viewBox="0 0 502 16" preserveAspectRatio="none" aria-hidden="true">
      <rect x="0" y="4" width="320" height="12" fill="var(--green)"/>
      <path d="M296 16 Q304 2 326 2 L502 2 L502 16 Z" fill="var(--paper)"/>
      <path d="M302 16 Q310 4 330 4 L502 4 L502 16 Z" fill="var(--navy)"/>
    </svg>
  </section>
</main>
</body>
</html>
```